Bluebonnet Tonic Lodge Label

I am looking to make a trendy and classy look for a label for our CBD products that's going on a green bottle and would like the writing on the label to be white I want a rustic farm look using different shades of green , I would like to keep it as Country Texas with the hipster flare as possible. I would like to keep it professional but look cool. I would like to incorporate the cross somewhere in there. We need room for nutriticianal facts info about the product i.e size of bottle fl , mg, and a qr code

```html
<!DOCTYPE html>
<html lang="en">
<head>
<meta charset="utf-8">
<title>Bluebonnet Tonic Lodge – CBD Oil Label</title>
<link rel="stylesheet" href="https://fonts.googleapis.com/css2?family=Roboto+Slab:wght@300;400;600&family=Roboto+Mono:wght@400&family=Oswald:wght@400&display=swap">
<style>
  :root {
    --page: #ffffff;
    --paper: #f3f4f0;
    --forest: #2f5b31;
    --forest-deep: #234a27;
    --lime: #a9c84a;
    --lime-soft: #c4d97a;
    --slate: #4d5866;
    --gold: #c9a94a;
    --gold-light: #e6d595;
    --ink: #1d1d1d;
    --white: #ffffff;
  }
  * { margin: 0; padding: 0; box-sizing: border-box; }
  html, body { width: 1200px; height: 1108px; overflow: hidden; background: var(--page); }
  .canvas {
    position: relative; width: 1200px; height: 1108px;
    display: flex; justify-content: center; align-items: center; gap: 60px;
  }
  .label {
    position: relative; width: 440px; height: 660px;
    font-family: "Roboto Slab", Georgia, serif;
  }
  .label--paper { background: var(--paper); box-shadow: 0 2px 10px rgba(0,0,0,.08); }
  .label--forest { background: var(--forest); }
  .label__frame { position: absolute; inset: 0; }
  .label__mark {
    position: absolute; left: 190px; top: 52px; width: 60px; height: 60px;
    background: var(--lime);
  }
  .label__est {
    position: absolute; top: 140px; width: 100%; text-align: center;
    font-size: 12px; letter-spacing: 2px; color: var(--gold);
  }
  .label__brand {
    position: absolute; top: 158px; width: 100%; text-align: center;
    font-size: 29px; font-weight: 400; color: var(--lime);
  }
  .label__place {
    position: absolute; top: 206px; width: 100%; text-align: center;
    font-family: "Roboto Mono", monospace; font-size: 12px; letter-spacing: 5px; color: var(--slate);
  }
  .label__band {
    position: absolute; left: 0; right: 0; top: 280px; height: 110px;
    background: var(--forest-deep);
    border-top: 2px solid var(--gold); border-bottom: 2px solid var(--gold);
    display: flex; justify-content: center; align-items: center; gap: 14px;
    font-size: 76px; font-weight: 300; line-height: 1;
  }
  .label__cbd { color: var(--lime-soft); }
  .label__oil { color: var(--white); }
  .label__formula {
    position: absolute; left: 150px; top: 408px;
    font-family: "Roboto Slab", Georgia, serif; font-weight: 600; font-size: 18px; color: var(--ink);
    border-top: 2px solid var(--lime); padding-top: 2px;
  }
  .label__formula sub { font-size: 11px; }
  .label__molecule {
    position: absolute; left: 52px; top: 420px; width: 180px; height: 90px;
    background: linear-gradient(135deg, rgba(169,200,74,.55), rgba(169,200,74,.2));
  }
  .label__strength {
    position: absolute; right: 58px; top: 436px;
    font-size: 58px; font-weight: 300; color: var(--lime);
  }
  .label--forest .label__strength { color: var(--forest-deep); }
  .label__ornament {
    position: absolute; left: 34px; right: 34px; top: 524px; height: 40px;
    background: linear-gradient(90deg, var(--gold-light), var(--gold), var(--gold-light));
  }
  .label__volume {
    position: absolute; top: 578px; width: 100%; text-align: center;
    font-family: "Oswald", "Arial Narrow", sans-serif; font-size: 22px; color: var(--ink);
  }
</style>
</head>
<body>
<main class="canvas">

  <section class="label label--paper">
    <svg class="label__frame" width="440" height="660" viewBox="0 0 440 660" aria-hidden="true">
      <polygon points="40,90 120,22 320,22 400,90 400,560 340,628 100,628 40,560" fill="var(--paper)" stroke="var(--gold)" stroke-width="2"/>
      <g stroke="var(--gold)" stroke-width="2">
        <line x1="8" y1="172" x2="40" y2="172"/><line x1="0" y1="180" x2="40" y2="180"/><line x1="8" y1="188" x2="40" y2="188"/>
        <line x1="400" y1="172" x2="432" y2="172"/><line x1="400" y1="180" x2="440" y2="180"/><line x1="400" y1="188" x2="432" y2="188"/>
      </g>
    </svg>
    <div class="label__mark"></div>
    <p class="label__est">EST. 2018</p>
    <h1 class="label__brand">Bluebonnet Tonic Lodge</h1>
    <p class="label__place">CEDAR HOLLOW + TEXAS</p>
    <div class="label__band"><span class="label__cbd">CBD</span><span class="label__oil">OIL</span></div>
    <div class="label__molecule" role="img" aria-label="Line drawing of the cannabidiol molecule structure"></div>
    <p class="label__formula">C<sub>21</sub>H<sub>30</sub>O<sub>2</sub></p>
    <p class="label__strength">4%</p>
    <div class="label__ornament" role="img" aria-label="Gold scrollwork ornament"></div>
    <p class="label__volume">30ML</p>
  </section>

  <section class="label label--forest">
    <svg class="label__frame" width="440" height="660" viewBox="0 0 440 660" aria-hidden="true">
      <polygon points="40,90 120,22 320,22 400,90 400,560 340,628 100,628 40,560" fill="var(--white)" stroke="var(--gold)" stroke-width="2"/>
      <g stroke="var(--gold)" stroke-width="2">
        <line x1="8" y1="172" x2="40" y2="172"/><line x1="0" y1="180" x2="40" y2="180"/><line x1="8" y1="188" x2="40" y2="188"/>
        <line x1="400" y1="172" x2="432" y2="172"/><line x1="400" y1="180" x2="440" y2="180"/><line x1="400" y1="188" x2="432" y2="188"/>
      </g>
    </svg>
    <div class="label__mark"></div>
    <p class="label__est">EST. 2018</p>
    <h1 class="label__brand">Bluebonnet Tonic Lodge</h1>
    <p class="label__place">CEDAR HOLLOW + TEXAS</p>
    <div class="label__band"><span class="label__cbd">CBD</span><span class="label__oil">OIL</span></div>
    <div class="label__molecule" role="img" aria-label="Line drawing of the cannabidiol molecule structure"></div>
    <p class="label__formula">C<sub>21</sub>H<sub>30</sub>O<sub>2</sub></p>
    <p class="label__strength">4%</p>
    <div class="label__ornament" role="img" aria-label="Gold scrollwork ornament"></div>
    <p class="label__volume">30ML</p>
  </section>

</main>
</body>
</html>
```